Math Help Website Needs New Design

Looking to refresh the design of my existing site (quillnumberdesk.com) to be easier on the eyes. I am fully capable of doing the HTML coding and have for years, but I don't have the eye for good design, colors, layout, and fonts. This is where I need help!

I need both a new design scheme and a new logo that matches. The overall functionality will be the same as the existing site, and should not be unrecognizable.

Target Market(s)

It should appeal to students (age 13-22) and their parents, so it should NOT be childish in appearance, nor should it be corporate.

Requirements
Must have
• Should be simple, easy-to-navigate, and neither childish nor corporate. I am looking for a design for both the homepage and a similar "content" page. Simple, bold colors are preferred. A logo should be prominent at the top, with a search bar nearby. Below that I need a similar navigational area like I already have. Then, I need about 200px wide ad space on the left of the main body area.

```html
<!DOCTYPE html>
<html lang="en">
<head>
<meta charset="utf-8">
<title>Quill Number Desk</title>
<link href="https://fonts.googleapis.com/css2?family=PT+Sans:wght@400;700&display=swap" rel="stylesheet">
<style>
:root{
  --dark:#242424;
  --frame:#1b1b1b;
  --page:#e8e8e8;
  --panel:#f4f4f4;
  --white:#ffffff;
  --green:#7cc400;
  --green-light:#99d60c;
  --green-dark:#5fa300;
  --text:#3a3a3a;
  --muted:#4e4e4e;
  --red:#e01515;
}
*{box-sizing:border-box;margin:0;padding:0}
html,body{width:972px;height:1200px;overflow:hidden}
body{position:relative;background:var(--page);font-family:"PT Sans",Arial,sans-serif;color:var(--text)}
.abs{position:absolute}
.top-band{left:0;top:0;width:972px;height:205px;background:var(--dark)}
.bottom-band{left:0;top:1093px;width:972px;height:107px;background:var(--dark)}
.brand{left:40px;top:26px;display:flex;align-items:center;gap:16px;font-size:30px;font-weight:700;color:var(--white)}
.brand-dot{width:44px;height:44px;border-radius:50%;background:var(--green)}
.search{left:735px;top:36px;width:218px;height:29px;border-radius:15px;background:#161616;border:2px solid #3a3a3a;color:#bdbdbd;font-size:12px;padding:5px 0 0 22px}
.search svg{position:absolute;right:10px;top:5px}
.frame{left:13px;top:88px;width:951px;height:1039px;background:var(--frame);border:1px solid #3a3a3a}
.panel{left:22px;top:99px;width:931px;height:1015px;background:var(--panel)}
.box{border:1px solid #dcdcdc;background:var(--white)}
.nav{width:897px;height:41px;display:flex;background:linear-gradient(#3a3a3a,#141414)}
.nav a{display:flex;align-items:center;justify-content:center;color:#f0f0f0;text-decoration:none;font-size:16px;border-right:1px solid #444}
.nav a.active{background:linear-gradient(var(--green-light),var(--green-dark))}
.hero{width:896px;height:284px;background:linear-gradient(var(--green-light),#6cb300)}
.hero-art{left:15px;top:14px;width:391px;height:255px;border:6px solid var(--white);background:linear-gradient(135deg,#3f6a4c,#7a5a3a 70%,#c08a55)}
.hero h1{left:437px;top:22px;font-size:25px;color:var(--white);font-weight:700}
.hero p{left:440px;width:410px;font-size:14px;line-height:20.5px;color:var(--white);text-align:justify}
.quiz{left:438px;top:223px;width:156px;height:39px;border-radius:20px;background:linear-gradient(#fafafa,#c9c9c9);color:#888;font-size:18px;font-weight:700;display:flex;align-items:center;justify-content:center}
.slider{left:648px;top:221px;width:154px;height:49px;background:rgba(255,255,255,.12)}
.features{width:904px;height:237px;background:linear-gradient(#2a2a2a,#1c1c1c);display:flex}
.feature{position:relative;flex:1;border-right:1px solid #3a3a3a}
.feature:last-child{border-right:0}
.scroll-rod{position:absolute;left:19px;top:17px;width:172px;height:10px;background:linear-gradient(#f2ede9,#9a8e86);border-radius:2px}
.scroll-card{position:absolute;left:25px;top:27px;width:160px;height:81px;background:linear-gradient(#fdfdfd,#dcdcdc);display:flex;align-items:center;justify-content:center;font-size:20px;font-weight:700;color:#444}
.feature ul{position:absolute;left:26px;top:125px;list-style:none;color:var(--white);font-size:12px;font-weight:700;line-height:20.5px}
.feature li::before{content:"";display:inline-block;width:7px;height:7px;border-radius:50%;background:var(--white);margin-right:9px;vertical-align:1px}
.chat{position:absolute;left:35px;width:165px;display:flex;gap:12px;color:var(--white);font-size:12px;font-weight:700;line-height:17px}
.chat span:last-child{width:122px}
.avatar{flex:none;width:25px;height:25px;background:#8a8a8a;margin-top:4px}
.more{position:absolute;right:17px;top:197px;height:27px;padding:0 10px;border-radius:6px;background:linear-gradient(var(--green-light),var(--green-dark));color:var(--white);font-size:14px;font-weight:700;display:flex;align-items:center;gap:5px}
.heading{font-size:24px;color:var(--text);font-weight:400}
.heading span{color:var(--green-dark)}
.class-art{width:274px;height:178px;background:linear-gradient(120deg,#d9e2e8,#c9a27f 45%,#e46a2a);box-shadow:0 3px 5px rgba(0,0,0,.25)}
.copy{font-size:13px;line-height:19.5px;color:var(--muted);text-align:justify}
.ad{width:192px;height:323px;border:1px solid #111;background:var(--white)}
.ad-photo{left:0;top:0;width:190px;height:156px;background:linear-gradient(#f4f4f4,#9bc3c8 60%,#3e4a3e)}
.ad-band{left:0;top:156px;width:190px;height:39px;background:var(--red);color:var(--white);font-size:20px;font-weight:700;display:flex;align-items:center;justify-content:center}
.ad-band sup{font-size:12px}
.ad-text{left:0;top:208px;width:190px;text-align:center;font-size:23px;font-weight:700;color:#111;line-height:22px}
.ad-btn{left:56px;top:284px;width:78px;height:25px;background:var(--red);color:var(--white);font-size:17px;font-weight:700;display:flex;align-items:center;justify-content:center}
.footer-nav{left:0;top:1146px;width:972px;display:flex;justify-content:center;color:var(--white);font-size:14px}
.footer-nav span{padding:0 17px}
.copyright{left:0;top:1176px;width:972px;text-align:center;color:var(--white);font-size:14px}
</style>
</head>
<body>
<div class="abs top-band"></div>
<div class="abs bottom-band"></div>

<header>
  <div class="abs brand"><span class="brand-dot"></span>Quill Number Desk</div>
  <div class="abs search">------Search here---------------
    <svg width="20" height="18" viewBox="0 0 20 18"><circle cx="7" cy="7" r="5" fill="none" stroke="#8ccf14" stroke-width="2.5"/><line x1="11" y1="11" x2="17" y2="16" stroke="#8ccf14" stroke-width="3" stroke-linecap="round"/></svg>
  </div>
</header>

<div class="abs frame"></div>
<main class="abs panel">
  <div class="abs box" style="left:10px;top:18px;width:914px;height:351px"></div>
  <nav class="abs nav" style="left:19px;top:26px">
    <a class="active" style="width:94px">Home</a>
    <a style="width:125px">Algebra</a>
    <a style="width:106px">Trig</a>
    <a style="width:132px">Geometry</a>
    <a style="width:117px">Calculus</a>
    <a style="width:142px">More Subjects</a>
    <a style="width:181px;border-right:0">Message Board</a>
  </nav>

  <section class="abs hero" style="left:19px;top:75px">
    <div class="abs hero-art" role="img" aria-label="Illustration of a teacher at a chalkboard with students"></div>
    <h1 class="abs">Welcome to Quill Number Desk ....</h1>
    <p class="abs" style="top:71px">Looking to understand a subject better, or maybe you don't understand what your textbook is trying to tell you? We have a collection of algebra and geometry lessons that you can view online right now.</p>
    <p class="abs" style="top:168px">Ask your question on our math help message board. Just be sure to explain what you've tried to do !!</p>
    <div class="abs quiz">TAKE A QUIZ !</div>
    <svg class="abs slider" viewBox="0 0 154 49">
      <circle cx="13" cy="23" r="11" fill="#fff" stroke="#555"/><path d="M15 17l-6 6 6 6" fill="none" stroke="#333" stroke-width="2.5"/>
      <circle cx="49" cy="23" r="6" fill="#555"/>
      <circle cx="78" cy="23" r="6" fill="#fff" stroke="#666"/>
      <circle cx="106" cy="23" r="6" fill="#fff" stroke="#666"/>
      <circle cx="139" cy="23" r="11" fill="#fff" stroke="#555"/><path d="M137 17l6 6-6 6" fill="none" stroke="#333" stroke-width="2.5"/>
    </svg>
  </section>

  <div class="abs box" style="left:10px;top:398px;width:914px;height:255px"></div>
  <section class="abs features" style="left:15px;top:407px">
    <div class="feature">
      <div class="scroll-rod"></div><div class="scroll-card">Whats New ?</div>
      <ul><li>Multiplying Polynomials</li><li>Derivatives of Logs and Exps</li><li>Differentiating Trig Functions</li></ul>
      <div class="more">View more ▸</div>
    </div>
    <div class="feature">
      <div class="scroll-rod"></div><div class="scroll-card">Math Lessons</div>
      <ul><li>Sports Maths</li><li>Algebra and Geometry</li><li>Trignometry and Calculas</li></ul>
      <div class="more">View more ▸</div>
    </div>
    <div class="feature">
      <div class="scroll-rod"></div><div class="scroll-card">Discussion</div>
      <ul><li>Geometry Posted by: Tolven</li><li>Interior Posted by: Tolven</li><li>Geometry Posted by: Tolven</li></ul>
      <div class="more">View more ▸</div>
    </div>
    <div class="feature">
      <div class="scroll-rod"></div><div class="scroll-card">Live Help</div>
      <div class="chat" style="top:120px"><span class="avatar"></span><span>anyone know french 1?? 2 replies</span></div>
      <div class="chat" style="top:155px"><span class="avatar"></span><span>anyone know french 1?? 2 replies</span></div>
      <div class="more">View more ▸</div>
    </div>
  </section>

  <aside class="abs ad" style="left:15px;top:671px">
    <div class="abs ad-photo" role="img" aria-label="Photo of two smiling students with books"></div>
    <div class="abs ad-band">Classes 4<sup>th</sup>&nbsp;- 12<sup>th</sup></div>
    <div class="abs ad-text">Worksheets<br>&amp;<br>Exercises</div>
    <div class="abs ad-btn">View</div>
  </aside>

  <h2 class="abs heading" style="left:225px;top:672px">The Perfect Online <span>Math Learing Class</span></h2>
  <div class="abs class-art" style="left:227px;top:721px" role="img" aria-label="Photo of students studying together at a table with books"></div>
  <p class="abs copy" style="left:521px;top:719px;width:394px">Lorem Ipsum is simply dummy text of the printing and typesetting industry. Lorem Ipsum has been the industry's standard dummy text ever since the 1500s, when an unknown printer took a galley of type and scrambled it to make a type specimen book. It has survived not only five centuries, but also the leap into electronic typesetting, remaining essentially unchanged. It was popularised in the 1960s with the release of Letraset sheets containing</p>
  <p class="abs copy" style="left:521px;top:869px;width:394px">Lorem Ipsum is simply dummy text of the printing and typesetting industry. Lorem Ipsum has been the industry's</p>
  <p class="abs copy" style="left:232px;top:922px;width:683px">Lorem Ipsum is simply dummy text of the printing and typesetting industry. Lorem Ipsum has been the industry's standard dummy text ever since the 1500s, when an unknown printer took a galley of type and scrambled it to make a type specimen book. It has survived not only five centuries, but also the leap into electronic typesetting</p>
</main>

<footer>
  <div class="abs footer-nav">
    <span>Home</span>|<span>Algebra</span>|<span>Trig</span>|<span>Geometry</span>|<span>Calculus</span>|<span>More Subjects</span>|<span>Message Board</span>
  </div>
  <div class="abs copyright">Copyright @ quillnumberdesk.com . All Right Reserved</div>
</footer>
</body>
</html>
```